New Business Card for General Contractor Marketing

Need a business card the is more like a marketing promotion of our services
Must be horizontal orientation, One Sided Only, Max font size, Organize the Services
#1 General Contractor for Realtors
Remodels – Renovations – Repairs
Water & Mold Damage Experts
Painting: Interior/ Exterior
Flooring: Wood / LVT / Carpet
Plumbing: Repairs & Upgrades
Electric: Lights & Energy Efficient Upgrades
Kitchen & Bath Remodels
Fast Inspections Repair Billed Thru Escrow
BrightHarborBuilds.com
555-418-2796

Industry/Entity Type

General Contractor

Contact Information for Business Card

One Sided Only: #1 General Contractor for Realtors Remodels – Renovations – Repairs Water & Mold Damage Experts Painting: Interior/ Exterior Flooring: Wood / LVT / Carpet Plumbing: Repairs & Upgrades Electric: Lights & Energy Efficient Upgrades Kitchen & Bath Remodels Fast Inspections Repair Billed Thru Escrow BrightHarborBuilds.com 555-418-2796

Colors
0054AA
0677BA
7BADD7
CADEEF
E8F1F8

Requirements
Must have
• One Sided Only: #1 General Contractor for Realtors Remodels – Renovations – Repairs Water & Mold Damage Experts Painting: Interior/ Exterior Flooring: Wood / LVT / Carpet Plumbing: Repairs & Upgrades Electric: Lights & Energy Efficient Upgrades Kitchen & Bath Remodels Fast Inspections Repair Billed Thru Escrow BrightHarborBuilds.com 555-418-2796

```html
<!DOCTYPE html>
<html lang="en">
<head>
<meta charset="utf-8">
<title>Bright Harbor Builds – Business Card</title>
<link rel="stylesheet" href="https://fonts.googleapis.com/css2?family=Roboto+Condensed:ital,wght@0,400;0,700;1,300;1,400;1,700&display=swap">
<style>
  :root {
    --backdrop: #9a9a9a;
    --navy: #1a2a54;
    --orange: #f58220;
    --white: #ffffff;
    --ink: #1a2a54;
  }
  * { margin: 0; padding: 0; box-sizing: border-box; }
  html, body {
    width: 1200px; height: 1059px; overflow: hidden;
    background: var(--backdrop);
    font-family: "Roboto Condensed", "Arial Narrow", sans-serif;
  }
  .card {
    position: absolute; left: 234px; top: 320px;
    width: 733px; height: 419px;
    background: var(--navy);
    border-radius: 24px;
    overflow: hidden;
    color: var(--white);
  }
  .brand-panel {
    position: absolute; left: 0; top: 0;
    width: 209px; height: 138px;
    background: var(--white);
    display: flex; align-items: center; justify-content: center; gap: 8px;
    padding: 0 12px;
  }
  .brand-mark { width: 18px; height: 18px; background: var(--orange); flex: none; }
  .brand-name {
    color: var(--ink); font-weight: 700; font-size: 22px; line-height: 1.05;
    text-transform: uppercase;
  }
  .headline {
    position: absolute; left: 209px; right: 0; top: 44px;
    text-align: center;
    color: var(--orange); font-weight: 700; font-size: 27.5px;
    letter-spacing: 0.1px; white-space: nowrap;
  }
  .subhead {
    position: absolute; left: 209px; right: 0; top: 81px;
    text-align: center; font-size: 25px; white-space: nowrap;
  }
  .services {
    position: absolute; top: 158px; list-style: none;
  }
  .services li {
    position: relative; height: 35px; line-height: 28px;
    padding-left: 23px; font-style: italic; font-weight: 400;
    font-size: 19.5px; white-space: nowrap;
  }
  .services li::before {
    content: ""; position: absolute; left: 0; top: 9px;
    width: 11px; height: 11px; border-radius: 50%; background: var(--orange);
  }
  .services-left { left: 30px; }
  .services-right { left: 340px; top: 160px; }
  .divider {
    position: absolute; left: 312px; top: 163px;
    width: 2px; height: 90px; background: var(--orange);
  }
  .tagline {
    position: absolute; left: 0; right: 0; top: 288px;
    text-align: center; font-weight: 700; font-style: italic;
    font-size: 30px; white-space: nowrap;
    display: flex; justify-content: center; align-items: center; gap: 9px;
  }
  .tagline .dot {
    width: 16px; height: 16px; border-radius: 50%; background: var(--orange);
  }
  .contact {
    position: absolute; top: 354px;
    display: flex; align-items: center; gap: 8px;
    font-size: 27px; white-space: nowrap;
  }
  .contact svg { flex: none; }
  .contact-web { left: 35px; }
  .contact-phone { right: 31px; top: 356px; }
</style>
</head>
<body>
  <main class="card">
    <div class="brand-panel">
      <span class="brand-mark"></span>
      <span class="brand-name">Bright Harbor<br>Builds</span>
    </div>

    <h1 class="headline">#1 GENERAL CONTRACTOR FOR REALTORS</h1>
    <p class="subhead">Remodels – Renovations – Repairs</p>

    <ul class="services services-left">
      <li>Water &amp; Mold Damage Experts</li>
      <li>Painting – Interior / Exterior</li>
      <li>Flooring – Wood / LVT / Carpet</li>
    </ul>
    <span class="divider"></span>
    <ul class="services services-right">
      <li>Plumbing – Repairs &amp; Upgrades</li>
      <li>Electrical – Lights &amp; Energy-Efficient Upgrades</li>
      <li>Kitchen &amp; Bath Remodels</li>
    </ul>

    <p class="tagline">FAST INSPECTIONS <span class="dot"></span> REPAIR BILLED THRU ESCROW</p>

    <p class="contact contact-web">
      <svg width="24" height="24" viewBox="0 0 24 24" aria-hidden="true">
        <circle cx="12" cy="12" r="11" fill="var(--orange)"/>
        <path d="M5 7c3 1 4 3 3 5s1 4 0 7M14 2c-1 3 2 4 4 4M20 14c-2 0-3 2-2 5" stroke="var(--navy)" stroke-width="2" fill="none"/>
      </svg>
      BrightHarborBuilds.com
    </p>
    <p class="contact contact-phone">
      <svg width="28" height="22" viewBox="0 0 28 22" aria-hidden="true">
        <path d="M1 7c0-4 6-6 13-6s13 2 13 6v2h-6V6c-2-1-4-1-7-1s-5 0-7 1v3H1z" fill="var(--orange)"/>
        <path d="M8 9h12l5 8v4H3v-4z" fill="var(--orange)"/>
        <g fill="var(--navy)">
          <rect x="10" y="12" width="2" height="2"/><rect x="13" y="12" width="2" height="2"/><rect x="16" y="12" width="2" height="2"/>
          <rect x="10" y="15" width="2" height="2"/><rect x="13" y="15" width="2" height="2"/><rect x="16" y="15" width="2" height="2"/>
        </g>
      </svg>
      555-418-2796
    </p>
  </main>
</body>
</html>
```